" Como uma clínica ! Uso essências e ativos em todas as práticas terapêuticas , por isso a escolha da palavra MORAVILA , em alemão que significa essências . Além da essência humana. Ok . Minha irmã faz e trabalha na parte da Holistica (reiki, florais etc). São práticas voltadas mais para a saúde. Nesse nome tem a palavra Zen. Tratamos o indivíduo como um todo. A Tricologia trata de calvícies, queda de cabelos e problemas no couro cabeludo. Estética visando o rejuvenescimento. Em resumo : SAÚDE e BEM ESTAR . Pode até ser criado em duas cores ou não . No sentindo de frisar o ZEN. MoraVILA . Preciso também checar o domínio. "

```html
<!DOCTYPE html>
<html lang="pt-BR">
<head>
<meta charset="utf-8">
<title>MoraVILA – Cartão de visita</title>
<link href="https://fonts.googleapis.com/css2?family=Montserrat:wght@400;500;600&display=swap" rel="stylesheet">
<style>
  :root {
    --page-bg: #e9e9ea;
    --card-black: #0c0c0c;
    --card-white: #ffffff;
    --gold: #c9a24a;
    --gold-light: #f3dc97;
    --gold-dark: #8e6a22;
    --ink: #1d1d1d;
    --muted: #6d6d6d;
  }
  * { margin: 0; padding: 0; box-sizing: border-box; }
  html, body { width: 1200px; height: 1200px; overflow: hidden; }
  body {
    background: var(--page-bg);
    font-family: "Montserrat", sans-serif;
    position: relative;
  }
  .card {
    position: absolute;
    left: 242px;
    width: 730px;
    height: 424px;
    border-radius: 34px;
    overflow: hidden;
  }
  .card-front { top: 137px; background: var(--card-black); }
  .card-back { top: 619px; background: var(--card-white); }

  .front-glow {
    position: absolute;
    left: 0; bottom: 0;
    width: 560px; height: 210px;
    background: radial-gradient(ellipse at 45% 75%, rgba(201,162,74,0.35), rgba(201,162,74,0) 65%);
  }
  .brand {
    position: absolute;
    text-align: center;
    color: var(--gold);
    font-weight: 500;
    letter-spacing: 1px;
    line-height: 1;
  }
  .brand-front { left: 0; right: 0; top: 208px; font-size: 82px; }
  .tagline {
    position: absolute;
    text-align: center;
    font-weight: 500;
    letter-spacing: 5px;
    line-height: 1;
  }
  .tagline-front { left: 0; right: 0; top: 298px; font-size: 19px; color: #f2f2f2; }

  .gold-edge {
    position: absolute;
    top: 0; right: 0;
    width: 26px; height: 100%;
    background: linear-gradient(180deg, var(--gold-dark), var(--gold-light) 45%, var(--gold) 70%, var(--gold-dark));
  }
  .name-tab {
    position: absolute;
    left: 0; top: 60px;
    width: 62px; height: 46px;
    background: linear-gradient(120deg, var(--gold-dark), var(--gold-light) 50%, var(--gold));
    border-radius: 0 0 24px 0;
  }
  .holder-name {
    position: absolute;
    left: 78px; top: 68px;
    font-size: 26px; font-weight: 500; color: var(--ink);
  }
  .contact-list {
    position: absolute;
    left: 46px; top: 152px;
    list-style: none;
  }
  .contact-list li {
    display: flex; align-items: center;
    height: 42px;
    font-size: 21px; color: var(--ink);
  }
  .contact-icon {
    width: 28px; height: 28px; margin-right: 14px;
    flex: none;
  }
  .address {
    position: absolute;
    left: 46px; top: 336px;
    font-size: 20px; line-height: 31px; color: var(--ink);
  }
  .brand-back { left: 360px; width: 330px; top: 208px; font-size: 54px; color: var(--gold); }
  .tagline-back { left: 360px; width: 330px; top: 272px; font-size: 13px; letter-spacing: 3.5px; color: var(--muted); }
</style>
</head>
<body>

<section class="card card-front">
  <div class="front-glow" role="img" aria-label="Ondas douradas decorativas"></div>
  <div class="brand brand-front">MoraVILA</div>
  <div class="tagline tagline-front">SAÚDE &amp; BEM ESTAR</div>
</section>

<section class="card card-back">
  <div class="name-tab"></div>
  <div class="holder-name">Helena Sato Ribeiro</div>

  <ul class="contact-list">
    <li>
      <svg class="contact-icon" viewBox="0 0 28 28"><circle cx="14" cy="14" r="14" fill="var(--gold)"/><path d="M10 7.5c1 0 1.6 2.6 1.6 3.2 0 .9-1.3 1.3-1.1 2 .6 1.8 2.2 3.4 3.9 4 .7.2 1.1-1.1 2-1.1.6 0 3.2.6 3.2 1.6 0 1.4-1.6 2.8-3.1 2.6-4.6-.6-8.5-4.5-9.1-9.1C7.2 9.1 8.6 7.5 10 7.5z" fill="#fff"/></svg>
      (11) 3481-0717
    </li>
    <li>
      <svg class="contact-icon" viewBox="0 0 28 28"><circle cx="14" cy="14" r="14" fill="var(--gold)"/><rect x="9.5" y="6.5" width="9" height="15" rx="1.6" fill="#fff"/><rect x="11" y="8.5" width="6" height="9.5" fill="var(--gold)"/></svg>
      (11) 987654321
    </li>
    <li>
      <svg class="contact-icon" viewBox="0 0 28 28"><circle cx="14" cy="14" r="14" fill="var(--gold)"/><rect x="7" y="9" width="14" height="10" rx="1" fill="#fff"/><path d="M7.5 9.6L14 14.5l6.5-4.9" fill="none" stroke="var(--gold)" stroke-width="1.4"/></svg>
      contato@moravila.com
    </li>
    <li>
      <svg class="contact-icon" viewBox="0 0 28 28"><circle cx="14" cy="14" r="14" fill="var(--gold)"/></svg>
      /moravila
    </li>
  </ul>

  <p class="address">Rua das Acácias, 250 | Centro<br>CEP: 01234-500 | Cidade/UF</p>

  <div class="brand brand-back">MoraVILA</div>
  <div class="tagline tagline-back">SAÚDE &amp; BEM ESTAR</div>

  <div class="gold-edge"></div>
</section>

</body>
</html>
```